Q&T Power Outfitters Business Cards

This will be used a business cards. Would love an industrial type flavor paired with the floating/3d is design like attached.

Do not have any certain colors picked out but something that will look good and stand out!!!.

Q&T Power Outfitters
"Don't be left in the dark"

The business does home standby Generators..

Contact Information for Business Card

Q&T Power Outfitters

Requirements
Must have
• Would love an industrial type flavor paired with the floating/3d is design like attached for a sample.

```html
<!DOCTYPE html>
<html lang="en">
<head>
<meta charset="utf-8">
<title>Q&amp;T Power Outfitters – Business Cards</title>
<link rel="stylesheet" href="https://fonts.googleapis.com/css2?family=Montserrat:wght@400;600;700&family=Nunito:ital,wght@1,600&display=swap">
<style>
  :root {
    --bg: #1b1b1b;
    --card: #070707;
    --blue: #0a5a92;
    --green: #8cc63f;
    --grey: #c9c9c9;
    --rule: #4a4a4a;
    --badge: #e8e8e8;
  }
  * { box-sizing: border-box; margin: 0; padding: 0; }
  html, body { width: 1200px; height: 900px; overflow: hidden; }
  body {
    background: var(--bg);
    font-family: "Montserrat", sans-serif;
    display: flex;
    align-items: center;
    justify-content: center;
    gap: 50px;
  }
  .card {
    position: relative;
    width: 540px;
    height: 309px;
    background: var(--card);
    border-radius: 3px;
  }
  .brand {
    display: flex;
    flex-direction: column;
    align-items: flex-start;
  }
  .brand-name {
    display: flex;
    align-items: center;
    gap: 10px;
    font-weight: 700;
    color: var(--blue);
    text-transform: uppercase;
    letter-spacing: 0.5px;
    white-space: nowrap;
  }
  .brand-dot {
    width: 14px; height: 14px;
    border-radius: 50%;
    background: var(--green);
    flex: none;
  }
  .tagline {
    font-family: "Nunito", sans-serif;
    font-style: italic;
    font-weight: 600;
    color: var(--green);
    margin-top: 4px;
    white-space: nowrap;
  }
  /* contact side */
  .card-front .brand { position: absolute; top: 58px; right: 48px; }
  .card-front .brand-name { font-size: 22px; }
  .card-front .tagline { font-size: 17px; padding-left: 24px; }
  .person { position: absolute; left: 36px; top: 176px; }
  .person-name { font-size: 20px; font-weight: 600; text-transform: uppercase; white-space: nowrap; }
  .first { color: var(--blue); }
  .last { color: var(--green); }
  .person-role { color: var(--grey); font-size: 13px; margin-top: 2px; }
  .divider {
    position: absolute; left: 96px; top: 214px;
    width: 260px; height: 1px; background: var(--rule);
  }
  .contacts {
    position: absolute; left: 36px; top: 230px;
    list-style: none;
    display: flex; flex-direction: column; gap: 5px;
    font-size: 12.5px; color: var(--grey);
  }
  .contacts li { display: flex; align-items: center; gap: 8px; white-space: nowrap; }
  .contacts svg { width: 17px; height: 17px; flex: none; }
  .contacts .accent { color: var(--green); }
  .partners {
    position: absolute; right: 28px; top: 160px;
    display: grid;
    grid-template-columns: 70px 70px;
    gap: 12px;
  }
  .partner-badge { height: 26px; background: var(--badge); border-radius: 2px; }
  .partner-badge.wide { grid-column: span 2; width: 110px; justify-self: end; }
  .partner-badge.diamond { background: #d8d8d8; }
  /* logo side */
  .card-back { display: flex; align-items: center; justify-content: center; }
  .card-back .brand-name { font-size: 28px; }
  .card-back .tagline { font-size: 21px; padding-left: 30px; }
</style>
</head>
<body>
  <section class="card card-front" aria-label="Business card, contact side">
    <div class="brand">
      <div class="brand-name"><span class="brand-dot"></span><span>Q&amp;T Power Outfitters</span></div>
      <p class="tagline">Don't be left in the dark</p>
    </div>

    <div class="person">
      <p class="person-name"><span class="first">Daniel</span> <span class="last">Whitford</span></p>
      <p class="person-role">Owner</p>
    </div>
    <div class="divider"></div>

    <ul class="contacts">
      <li>
        <svg viewBox="0 0 20 20"><circle cx="10" cy="10" r="9" fill="none" stroke="var(--green)" stroke-width="2"/><path d="M7 6l2 2-1 1.5a6 6 0 0 0 2.5 2.5L12 11l2 2-1.5 1.5C9 14 6 11 5.5 7.5z" fill="var(--green)"/></svg>
        <span class="contact-text">409-555-0187</span>
      </li>
      <li>
        <svg viewBox="0 0 20 20"><circle cx="10" cy="10" r="9" fill="none" stroke="var(--green)" stroke-width="2"/><rect x="5.5" y="7" width="9" height="6.5" fill="var(--green)"/><path d="M5.5 7l4.5 3.5L14.5 7" fill="none" stroke="var(--card)" stroke-width="1"/></svg>
        <span class="contact-text">Sales@qtpoweroutfitters.com</span>
      </li>
      <li>
        <svg viewBox="0 0 20 20"><circle cx="10" cy="10" r="9" fill="none" stroke="var(--green)" stroke-width="2"/><circle cx="10" cy="10" r="5" fill="none" stroke="var(--green)" stroke-width="1.3"/><path d="M5 10h10M10 5c-2 3-2 7 0 10M10 5c2 3 2 7 0 10" fill="none" stroke="var(--green)" stroke-width="1"/></svg>
        <span class="contact-text">www.<span class="accent">qtpoweroutfitters</span>.com</span>
      </li>
    </ul>

    <div class="partners" aria-label="Partner brands">
      <div class="partner-badge wide"></div>
      <div class="partner-badge"></div>
      <div class="partner-badge"></div>
      <div class="partner-badge diamond"></div>
      <div class="partner-badge"></div>
    </div>
  </section>

  <section class="card card-back" aria-label="Business card, brand side">
    <div class="brand">
      <div class="brand-name"><span class="brand-dot"></span><span>Q&amp;T Power Outfitters</span></div>
      <p class="tagline">Don't be left in the dark</p>
    </div>
  </section>
</body>
</html>
```